Poster for Stores

We need a poster design for my company, ourcornerville.net. The company is a social networking site oriented around the town.

I have a slogan for the site....Helping Town Connect with People.

I want the background color to be a type of green.

I want to have a picture of a generic town in the background.

I would some of the below text in the poster to be:

1) All your local town deals in one place.
2) its's free..no cost
3) create town events...create groups...blog or forum about/around the town.
4) find out about city/town services

Industry/Entity Type

Town

```html
<!DOCTYPE html>
<html lang="en">
<head>
<meta charset="utf-8">
<title>ourcornerville.net — Poster</title>
<link href="https://fonts.googleapis.com/css2?family=Source+Sans+3:wght@400;600;700&display=swap" rel="stylesheet">
<style>
  :root {
    --sky-top: #a9dcf3;
    --sky-mid: #c4e9f8;
    --building-yellow: #f6cf5a;
    --building-orange: #ec8a45;
    --building-teal: #6cc5a4;
    --town-orange: #f2a03a;
    --green-deep: #45b549;
    --green-light: #8cc63f;
    --footer-green: #a8cf3a;
    --accent-orange: #f7941d;
    --white: #ffffff;
  }
  * { box-sizing: border-box; margin: 0; padding: 0; }
  html, body { width: 849px; height: 1200px; overflow: hidden; }
  body { font-family: "Source Sans 3", "Helvetica Neue", Arial, sans-serif; }

  .poster {
    position: relative;
    width: 849px;
    height: 1200px;
    background: var(--white);
    overflow: hidden;
  }

  .town-scene {
    position: absolute;
    left: 0; top: 0;
    width: 849px; height: 492px;
    background: linear-gradient(to bottom,
      var(--sky-top) 0%,
      var(--sky-mid) 28%,
      var(--building-yellow) 52%,
      var(--building-orange) 72%,
      var(--building-teal) 100%);
  }

  .divider { position: absolute; left: 0; width: 849px; }
  .divider--top { top: 492px; height: 16px; }
  .divider--bottom { top: 1114px; height: 18px; }

  .main-panel {
    position: absolute;
    left: 0; top: 508px;
    width: 849px; height: 606px;
    background: linear-gradient(to bottom, var(--green-deep) 0%, var(--green-deep) 55%, var(--green-light) 100%);
  }

  .site-name {
    position: absolute;
    left: 0; top: 36px;
    width: 100%;
    text-align: center;
    color: var(--white);
    font-weight: 600;
    font-size: 94px;
    line-height: 1;
    letter-spacing: 0.5px;
  }

  .slogan {
    position: absolute;
    left: 0; top: 174px;
    width: 100%;
    text-align: center;
    color: var(--accent-orange);
    font-weight: 700;
    font-size: 48px;
    line-height: 1;
    text-shadow:
      -2px -2px 0 var(--white), 2px -2px 0 var(--white),
      -2px 2px 0 var(--white), 2px 2px 0 var(--white),
      0 2px 0 var(--white), 0 -2px 0 var(--white),
      2px 0 0 var(--white), -2px 0 0 var(--white);
  }

  .features {
    position: absolute;
    left: 108px; top: 262px;
    list-style: none;
  }
  .feature {
    display: flex;
    align-items: center;
    height: 65px;
    color: var(--white);
    font-weight: 600;
    font-size: 29px;
  }
  .feature--highlight { font-weight: 700; }
  .feature__star { width: 36px; height: 36px; margin-right: 20px; flex: none; }

  .footer {
    position: absolute;
    left: 0; top: 1132px;
    width: 849px; height: 68px;
    background: var(--footer-green);
    color: var(--white);
    text-align: center;
    font-size: 19px;
    line-height: 70px;
  }
</style>
</head>
<body>
<div class="poster">
  <div class="town-scene" role="img" aria-label="Illustrated skyline of a generic town with colourful tall buildings, a town hall with a clock, small houses, trees and a sun among clouds"></div>

  <svg class="divider divider--top" viewBox="0 0 849 16" preserveAspectRatio="none">
    <rect x="0" y="0" width="849" height="5" fill="var(--white)"/>
    <rect x="0" y="5" width="849" height="5" fill="var(--town-orange)"/>
    <rect x="0" y="10" width="849" height="6" fill="var(--white)"/>
  </svg>

  <section class="main-panel">
    <h1 class="site-name">ourcornerville.net</h1>
    <p class="slogan">Helping Town Connect with People</p>

    <ul class="features">
      <li class="feature">
        <svg class="feature__star" viewBox="0 0 36 36"><polygon points="18,2 22.6,13 34,13.5 25,21 28,33 18,26.5 8,33 11,21 2,13.5 13.4,13" fill="var(--accent-orange)" stroke="var(--white)" stroke-width="2" stroke-linejoin="round"/></svg>
        All your local deals in one place.
      </li>
      <li class="feature">
        <svg class="feature__star" viewBox="0 0 36 36"><polygon points="18,2 22.6,13 34,13.5 25,21 28,33 18,26.5 8,33 11,21 2,13.5 13.4,13" fill="var(--accent-orange)" stroke="var(--white)" stroke-width="2" stroke-linejoin="round"/></svg>
        Promote your town events.
      </li>
      <li class="feature">
        <svg class="feature__star" viewBox="0 0 36 36"><polygon points="18,2 22.6,13 34,13.5 25,21 28,33 18,26.5 8,33 11,21 2,13.5 13.4,13" fill="var(--accent-orange)" stroke="var(--white)" stroke-width="2" stroke-linejoin="round"/></svg>
        Create groups, blogs or forums about your town.
      </li>
      <li class="feature">
        <svg class="feature__star" viewBox="0 0 36 36"><polygon points="18,2 22.6,13 34,13.5 25,21 28,33 18,26.5 8,33 11,21 2,13.5 13.4,13" fill="var(--accent-orange)" stroke="var(--white)" stroke-width="2" stroke-linejoin="round"/></svg>
        Find out about your local city/town services.
      </li>
      <li class="feature feature--highlight">
        <svg class="feature__star" viewBox="0 0 36 36"><polygon points="18,2 22.6,13 34,13.5 25,21 28,33 18,26.5 8,33 11,21 2,13.5 13.4,13" fill="var(--accent-orange)" stroke="var(--white)" stroke-width="2" stroke-linejoin="round"/></svg>
        Its's all free and free to join!
      </li>
    </ul>
  </section>

  <svg class="divider divider--bottom" viewBox="0 0 849 18" preserveAspectRatio="none">
    <rect x="0" y="0" width="849" height="4" fill="var(--white)"/>
    <rect x="0" y="4" width="849" height="5" fill="var(--town-orange)"/>
    <rect x="0" y="9" width="849" height="4" fill="var(--white)"/>
    <rect x="0" y="13" width="849" height="5" fill="var(--town-orange)"/>
  </svg>

  <footer class="footer">Please visit ourcornerville.net to learn more.</footer>
</div>
</body>
</html>
```